Swing Tags for Kids Kustom Kulture clothing label

We are a new Kids clothing company that represents the Kustom Kulture. We need a design for our swing tags for the girls clothing range "Mabel Moppet"

We want a design that represents the culture, attitude and style of the Kustom Kulture ( Hot Rod/ Kustom cars / pin-up/ Rockabilly) scene.

We looking for a design for the front and back of our swing tag, no generic clip art, must be a original and creative design.

The size of the tag needs to be approx. 100mm x 50mm but we are open to different shapes .

the final files need to be in vector and PDF
Please have a look on our Friendwave page to see what we are all about.
https://www.friendwave.example/MabelMoppetClothing

Attached is our logo and some swing tag examples that we like.

Target Market(s)

The age group is 4 to 12 years old girls.
Kustom Kulture, Hot Rod, Pin-up, Rockabilly.

Industry/Entity Type

Clothing

Font styles to use
Serif
Sans Serif
Decorative
Script

Requirements
Must have
• The artwork needs to use our "Mabel Moppet" logo in the design on the Front and the following details need to be put on the back:
• -Style
• - Size
• - Price
• - website: www.mabelmoppet.example.au
• - Friendwave page www.friendwave.example/mabelmoppetclothing
Should not have
• Nudity , Bad Language .

```html
<!DOCTYPE html>
<html lang="en">
<head>
<meta charset="utf-8">
<title>Mabel Moppet Swing Tags</title>
<link href="https://fonts.googleapis.com/css2?family=Lobster&family=UnifrakturMaguntia&family=Oswald:wght@500&display=swap" rel="stylesheet">
<style>
  :root {
    --ink: #1a1414;
    --paper: #ffffff;
    --badge-blue: #2f4f95;
  }
  html, body { margin: 0; padding: 0; width: 1000px; height: 1200px; overflow: hidden; background: var(--paper); }
  .sheet { position: relative; width: 1000px; height: 1200px; }
  .tag { position: absolute; width: 460px; height: 240px; }
  .tag svg { display: block; width: 460px; height: 240px; overflow: visible; }

  .row-violet  { --base: #a24aa6; --band: #f4d800; --side: #2a1a2e; --card: #ece824; --accent: #f07a20; --accent-soft: #f6b04a; --name: #1a1414; --burst: #f4d800; }
  .row-sun     { --base: #f2e81c; --band: #1e2660; --side: #1e2660; --card: #f7b98a; --accent: #4a2a14; --accent-soft: #8a5a34; --name: #f7b98a; --burst: #b8262a; }
  .row-cherry  { --base: #e8262a; --band: #ffffff; --side: #1a1a1a; --card: #ffffff; --accent: #f3d21a; --accent-soft: #f7e36a; --name: #1a1414; --burst: #ffffff; }
  .row-clover  { --base: #3faa3a; --band: #e61e34; --side: #1a1a1a; --card: #fbf28a; --accent: #e0242a; --accent-soft: #f06a5a; --name: #f7c9a0; --burst: #e61e34; }

  .outline { fill: var(--base); stroke: var(--ink); stroke-width: 3; }
  .hole { fill: var(--paper); stroke: var(--ink); stroke-width: 1.5; }
  .frame { fill: none; stroke: var(--ink); stroke-width: 2.5; }
  .band { fill: var(--band); stroke: var(--ink); stroke-width: 2; }
  .side-panel { fill: var(--side); stroke: var(--ink); stroke-width: 2; }
  .card { fill: var(--card); stroke: var(--ink); stroke-width: 2.5; }
  .stop-burst { stop-color: var(--burst); }
  .stop-accent { stop-color: var(--accent); }
  .stop-accent-soft { stop-color: var(--accent-soft); }

  .brand-name { font-family: 'Lobster', cursive; font-size: 58px; fill: var(--name); }
  .field-label { font-family: 'UnifrakturMaguntia', serif; font-size: 17px; fill: var(--ink); }
  .field-line { stroke: var(--ink); stroke-width: 1.2; }
  .badge-box { fill: var(--paper); stroke: var(--badge-blue); stroke-width: 2; }
  .badge-square { fill: var(--badge-blue); }
  .badge-small { font-family: 'Oswald', sans-serif; font-size: 12px; fill: var(--badge-blue); }
  .badge-name { font-family: 'Oswald', sans-serif; font-size: 15px; fill: var(--badge-blue); }
  .web-address { font-family: 'UnifrakturMaguntia', serif; font-size: 10px; fill: var(--ink); }
</style>
</head>
<body>
<svg width="0" height="0" style="position:absolute" aria-hidden="true">
  <defs>
    <symbol id="tag-outline" viewBox="0 0 460 240">
      <path d="M230,2 L242,42 C262,48 285,46 300,58 C330,52 355,60 370,74 L442,74 L456,96 L456,160 L444,182 L392,186 C372,206 340,222 300,226 L160,226 C120,222 88,206 68,186 L16,182 L4,160 L4,96 L18,74 L90,74 C105,60 130,52 160,58 C175,46 198,48 218,42 Z"/>
    </symbol>
  </defs>
</svg>

<main class="sheet">
  <!-- Row 1 -->
  <section class="tag tag-front row-violet" style="left:38px; top:28px;">
    <svg viewBox="0 0 460 240">
      <defs><radialGradient id="burst-1" cx="50%" cy="30%" r="60%"><stop offset="0" class="stop-burst"/><stop offset="1" class="stop-burst" stop-opacity="0"/></radialGradient></defs>
      <use href="#tag-outline" class="outline"/>
      <circle class="hole" cx="230" cy="48" r="6"/>
      <rect class="frame" x="18" y="82" width="424" height="98"/>
      <rect class="band" x="30" y="92" width="400" height="78"/>
      <rect x="120" y="170" width="250" height="50" fill="url(#burst-1)" role="img" aria-label="Sunburst rays fanning out beneath the name"/>
      <text class="brand-name" x="230" y="148" text-anchor="middle">Mabel Moppet</text>
    </svg>
  </section>
  <section class="tag tag-back row-violet" style="left:508px; top:28px;">
    <svg viewBox="0 0 460 240">
      <defs><linearGradient id="scroll-1" x1="0" x2="1"><stop offset="0" class="stop-accent-soft"/><stop offset=".5" class="stop-accent"/><stop offset="1" class="stop-accent-soft"/></linearGradient></defs>
      <use href="#tag-outline" class="outline"/>
      <circle class="hole" cx="230" cy="48" r="6"/>
      <rect class="side-panel" x="16" y="84" width="428" height="98"/>
      <rect class="card" x="60" y="78" width="340" height="104"/>
      <text class="field-label" x="70" y="106">Style:</text><line class="field-line" x1="112" y1="108" x2="200" y2="108"/>
      <text class="field-label" x="70" y="130">Size:</text><line class="field-line" x1="112" y1="132" x2="200" y2="132"/>
      <text class="field-label" x="70" y="154">Price:</text><line class="field-line" x1="112" y1="156" x2="200" y2="156"/>
      <rect class="badge-box" x="268" y="88" width="124" height="44"/>
      <rect class="badge-square" x="274" y="94" width="32" height="32"/>
      <text class="badge-small" x="312" y="106">Like us on</text>
      <text class="badge-name" x="312" y="125">Friendwave</text>
      <text class="web-address" x="392" y="150" text-anchor="end">friendwave.example/MabelMoppetClothing</text>
      <text class="web-address" x="392" y="166" text-anchor="end">www.mabelmoppet.example.au</text>
      <rect x="110" y="184" width="240" height="30" rx="15" fill="url(#scroll-1)" role="img" aria-label="Ornamental scrolls and ribbon bow"/>
    </svg>
  </section>

  <!-- Row 2 -->
  <section class="tag tag-front row-sun" style="left:38px; top:288px;">
    <svg viewBox="0 0 460 240">
      <defs><radialGradient id="burst-2" cx="50%" cy="30%" r="60%"><stop offset="0" class="stop-burst"/><stop offset="1" class="stop-burst" stop-opacity="0"/></radialGradient></defs>
      <use href="#tag-outline" class="outline"/>
      <circle class="hole" cx="230" cy="48" r="6"/>
      <rect class="frame" x="18" y="82" width="424" height="98"/>
      <rect class="band" x="30" y="92" width="400" height="78"/>
      <rect x="120" y="170" width="250" height="50" fill="url(#burst-2)" role="img" aria-label="Sunburst rays fanning out beneath the name"/>
      <text class="brand-name" x="230" y="148" text-anchor="middle">Mabel Moppet</text>
    </svg>
  </section>
  <section class="tag tag-back row-sun" style="left:508px; top:288px;">
    <svg viewBox="0 0 460 240">
      <defs><linearGradient id="scroll-2" x1="0" x2="1"><stop offset="0" class="stop-accent-soft"/><stop offset=".5" class="stop-accent"/><stop offset="1" class="stop-accent-soft"/></linearGradient></defs>
      <use href="#tag-outline" class="outline"/>
      <circle class="hole" cx="230" cy="48" r="6"/>
      <rect class="side-panel" x="16" y="84" width="428" height="98"/>
      <rect class="card" x="60" y="78" width="340" height="104"/>
      <text class="field-label" x="70" y="106">Style:</text><line class="field-line" x1="112" y1="108" x2="200" y2="108"/>
      <text class="field-label" x="70" y="130">Size:</text><line class="field-line" x1="112" y1="132" x2="200" y2="132"/>
      <text class="field-label" x="70" y="154">Price:</text><line class="field-line" x1="112" y1="156" x2="200" y2="156"/>
      <rect class="badge-box" x="268" y="88" width="124" height="44"/>
      <rect class="badge-square" x="274" y="94" width="32" height="32"/>
      <text class="badge-small" x="312" y="106">Like us on</text>
      <text class="badge-name" x="312" y="125">Friendwave</text>
      <text class="web-address" x="392" y="150" text-anchor="end">friendwave.example/MabelMoppetClothing</text>
      <text class="web-address" x="392" y="166" text-anchor="end">www.mabelmoppet.example.au</text>
      <rect x="110" y="184" width="240" height="30" rx="15" fill="url(#scroll-2)" role="img" aria-label="Ornamental scrolls and ribbon bow"/>
    </svg>
  </section>

  <!-- Row 3 -->
  <section class="tag tag-front row-cherry" style="left:38px; top:574px;">
    <svg viewBox="0 0 460 240">
      <defs><radialGradient id="burst-3" cx="50%" cy="30%" r="60%"><stop offset="0" class="stop-burst"/><stop offset="1" class="stop-burst" stop-opacity="0"/></radialGradient></defs>
      <use href="#tag-outline" class="outline"/>
      <circle class="hole" cx="230" cy="48" r="6"/>
      <rect class="frame" x="18" y="82" width="424" height="98"/>
      <rect class="band" x="30" y="92" width="400" height="78"/>
      <rect x="120" y="170" width="250" height="50" fill="url(#burst-3)" role="img" aria-label="Sunburst rays fanning out beneath the name"/>
      <text class="brand-name" x="230" y="148" text-anchor="middle">Mabel Moppet</text>
    </svg>
  </section>
  <section class="tag tag-back row-cherry" style="left:508px; top:574px;">
    <svg viewBox="0 0 460 240">
      <defs><linearGradient id="scroll-3" x1="0" x2="1"><stop offset="0" class="stop-accent-soft"/><stop offset=".5" class="stop-accent"/><stop offset="1" class="stop-accent-soft"/></linearGradient></defs>
      <use href="#tag-outline" class="outline"/>
      <circle class="hole" cx="230" cy="48" r="6"/>
      <rect class="side-panel" x="16" y="84" width="428" height="98"/>
      <rect class="card" x="60" y="78" width="340" height="104"/>
      <text class="field-label" x="70" y="106">Style:</text><line class="field-line" x1="112" y1="108" x2="200" y2="108"/>
      <text class="field-label" x="70" y="130">Size:</text><line class="field-line" x1="112" y1="132" x2="200" y2="132"/>
      <text class="field-label" x="70" y="154">Price:</text><line class="field-line" x1="112" y1="156" x2="200" y2="156"/>
      <rect class="badge-box" x="268" y="88" width="124" height="44"/>
      <rect class="badge-square" x="274" y="94" width="32" height="32"/>
      <text class="badge-small" x="312" y="106">Like us on</text>
      <text class="badge-name" x="312" y="125">Friendwave</text>
      <text class="web-address" x="392" y="150" text-anchor="end">friendwave.example/MabelMoppetClothing</text>
      <text class="web-address" x="392" y="166" text-anchor="end">www.mabelmoppet.example.au</text>
      <rect x="110" y="184" width="240" height="30" rx="15" fill="url(#scroll-3)" role="img" aria-label="Ornamental scrolls and ribbon bow"/>
    </svg>
  </section>

  <!-- Row 4 -->
  <section class="tag tag-front row-clover" style="left:38px; top:884px;">
    <svg viewBox="0 0 460 240">
      <defs><radialGradient id="burst-4" cx="50%" cy="30%" r="60%"><stop offset="0" class="stop-burst"/><stop offset="1" class="stop-burst" stop-opacity="0"/></radialGradient></defs>
      <use href="#tag-outline" class="outline"/>
      <circle class="hole" cx="230" cy="48" r="6"/>
      <rect class="frame" x="18" y="82" width="424" height="98"/>
      <rect class="band" x="30" y="92" width="400" height="78"/>
      <rect x="120" y="170" width="250" height="50" fill="url(#burst-4)" role="img" aria-label="Sunburst rays fanning out beneath the name"/>
      <text class="brand-name" x="230" y="148" text-anchor="middle">Mabel Moppet</text>
    </svg>
  </section>
  <section class="tag tag-back row-clover" style="left:508px; top:884px;">
    <svg viewBox="0 0 460 240">
      <defs><linearGradient id="scroll-4" x1="0" x2="1"><stop offset="0" class="stop-accent-soft"/><stop offset=".5" class="stop-accent"/><stop offset="1" class="stop-accent-soft"/></linearGradient></defs>
      <use href="#tag-outline" class="outline"/>
      <circle class="hole" cx="230" cy="48" r="6"/>
      <rect class="side-panel" x="16" y="84" width="428" height="98"/>
      <rect class="card" x="60" y="78" width="340" height="104"/>
      <text class="field-label" x="70" y="106">Style:</text><line class="field-line" x1="112" y1="108" x2="200" y2="108"/>
      <text class="field-label" x="70" y="130">Size:</text><line class="field-line" x1="112" y1="132" x2="200" y2="132"/>
      <text class="field-label" x="70" y="154">Price:</text><line class="field-line" x1="112" y1="156" x2="200" y2="156"/>
      <rect class="badge-box" x="268" y="88" width="124" height="44"/>
      <rect class="badge-square" x="274" y="94" width="32" height="32"/>
      <text class="badge-small" x="312" y="106">Like us on</text>
      <text class="badge-name" x="312" y="125">Friendwave</text>
      <text class="web-address" x="392" y="150" text-anchor="end">friendwave.example/MabelMoppetClothing</text>
      <text class="web-address" x="392" y="166" text-anchor="end">www.mabelmoppet.example.au</text>
      <rect x="110" y="184" width="240" height="30" rx="15" fill="url(#scroll-4)" role="img" aria-label="Ornamental scrolls and ribbon bow"/>
    </svg>
  </section>
</main>
</body>
</html>
```